Blow Dry Bar Business Cards

These cards must be eye catching and modern.
You must be willing to work fast and make changes.

Winner will be offered other projects

Files 1 THIS IS THE STYLE CARDS I AM INTRESTED IN!!!
Please be creative, I am paying for my own eye catching design. I need files to be quilla press ready.

COLORS THAT ARE PAINTED INSIDE MY SHOP:
- - - http://www.brennacoat.example/en/explore-colors/painter/color-selector.html?colors=4007-3C

- - - http://www.marlowtint.example/color/paint-colors/quiet-harbor-d58-2

I want the business cards sleek and modern if you use the logo please correct imperfections. I added the part that says Blow Dry Bar (see website).
Do not be afraid to separate the blow dryer from the name to make the cards look like the file with the pink elephant.

SHOULD INCLUDE
*Blow Dryer (we are a blow dry bar not a salon we do not cut or color so do not include sheers of any kind)
*BUSINESS NAME: Simply Swept Up - Blow Dry Bar (PLEASE SEE MY WEBSITE)
* Website: SIMPLYSWEPTUP.EXAMPLE
*Phone number (555) 314-7720
Updates

Quilla press said it can be submitted in JPG

http://www.marlowtint.example/color/paint-colors/quiet-harbor-d58-2 http://www.brennacoat.example/en/explore-colors/painter/color-selector.html?colors=4007-3C ^^^^ These links will take you to the color paint that is painted inside my shop.

Target Market(s)

AGES 18 - 55 WOMEN
HIGH END MARKET

Industry/Entity Type

Salon

Requirements
Must have
• SEE COLOR EXAMPLE FILE
BLOW DRYER
UNIQUE
I LIKE THE CARD WITH THE PINK ELEPHANT THE BEST
Nice to have
• BE AS CREATIVE AND MODERN AS POSSIBLE DO NOT COPY ANY OF THE CARDS BELOW.
Should not have
• SCISSORS
PINK

```html
<!DOCTYPE html>
<html lang="en">
<head>
<meta charset="utf-8">
<title>Simply Swept Up – Business Cards</title>
<link rel="stylesheet" href="https://fonts.googleapis.com/css2?family=Arvo&family=Lato:wght@400;700&display=swap">
<style>
  :root {
    --backdrop: #e7e4df;
    --card-dark: #0c0c0d;
    --card-teal: #58c8d0;
    --accent-teal: #4fc6cf;
    --ink-light: #f2f2f2;
    --ink-muted: #b9b9b9;
    --white: #ffffff;
  }
  * { margin: 0; padding: 0; box-sizing: border-box; }
  html, body { width: 1200px; height: 795px; overflow: hidden; }
  body {
    background: var(--backdrop);
    font-family: "Lato", sans-serif;
    position: relative;
  }
  .card {
    position: absolute;
    top: 252px;
    width: 500px;
    height: 290px;
    border-radius: 24px;
  }
  .card--front { left: 60px; background: var(--card-dark); padding: 30px 34px; }
  .card--back {
    left: 640px;
    background: var(--card-teal);
    display: flex;
    align-items: center;
    justify-content: center;
    gap: 18px;
  }
  .brand-name {
    font-family: "Arvo", serif;
    font-weight: 400;
    color: var(--accent-teal);
    font-size: 32px;
    line-height: 1;
  }
  .contact-person { margin-top: 26px; }
  .person-name { color: var(--accent-teal); font-weight: 700; font-size: 17px; }
  .person-role { color: var(--ink-muted); font-size: 13px; margin-top: 2px; }
  .business-details { margin-top: 18px; font-size: 13px; line-height: 1.4; color: var(--ink-light); }
  .business-title { color: var(--accent-teal); }
  .contact-lines { margin-top: 14px; font-size: 13px; line-height: 1.6; color: var(--ink-light); }
  .contact-line { display: flex; align-items: center; gap: 7px; }
  .contact-icon { width: 12px; height: 12px; flex: none; }
  .back-name {
    font-family: "Arvo", serif;
    font-weight: 400;
    color: var(--white);
    font-size: 40px;
    line-height: 1;
  }
  .back-mark { width: 26px; height: 26px; border-radius: 50%; background: var(--white); }
</style>
</head>
<body>
  <section class="card card--front" aria-label="Business card front">
    <h1 class="brand-name">Swept Up</h1>
    <div class="contact-person">
      <p class="person-name">Dana Reyes</p>
      <p class="person-role">Owner</p>
    </div>
    <address class="business-details" style="font-style:normal">
      <p class="business-title">Simply Swept Up - Blow Dry Bar</p>
      <p>82 Harbor Bend Road</p>
      <p>Suite 4 Alder Cove, texas 75099</p>
    </address>
    <div class="contact-lines">
      <p class="contact-line">
        <svg class="contact-icon" viewBox="0 0 12 12" aria-hidden="true"><path d="M2 1h2.5l1 3-1.5 1a6 6 0 0 0 3 3l1-1.5 3 1V10a1 1 0 0 1-1 1A9 9 0 0 1 1 2a1 1 0 0 1 1-1z" fill="var(--accent-teal)"/></svg>
        (555) 314-7720
      </p>
      <p class="contact-line">
        <svg class="contact-icon" viewBox="0 0 12 12" aria-hidden="true"><circle cx="6" cy="6" r="5.2" fill="none" stroke="var(--accent-teal)" stroke-width="1.2"/><path d="M1 6h10M6 1c-2.5 3-2.5 7 0 10M6 1c2.5 3 2.5 7 0 10" fill="none" stroke="var(--accent-teal)" stroke-width="1"/></svg>
        WWW.SIMPLYSWEPTUP.EXAMPLE
      </p>
    </div>
  </section>

  <section class="card card--back" aria-label="Business card back">
    <span class="back-name">Simply Swept Up</span>
    <span class="back-mark" aria-hidden="true"></span>
  </section>
</body>
</html>
```